"Global Leadership & Talent Development Firm" needs a website upgrade

Website Design Project is intended to find a vendor to update and provide maintenance for my website: www.Brightpath7Gains.com. I am looking for a vendor who is an expert with WordPress and eCommerce plugin.

Website Requirements
www.Brightpath7Gains.com

• Media Library (review)- Add video/utube
• Others (plug-ins)
1) eCommerce ability
a) Must have the ability to charge for the eLearning courses
i) Handle credit card processing
ii) Ability to handle yearly subscriptions
iii) Ability to process credits/refunds

Website Updates Assessment Page:
• Totally MORV- Distributor Information
• 4 Crew Patterns Assessment & logo
• Steering Quest- 360 Assessment
• Emotional Intelligence Assessment
Home & Tool Pages:
• K7V License and certification
• PulseCore Trainer
• 4 Crew Patterns training
Client & Contact Pages
• Update Client list
• Update testimonials
Speaker Page Update
Website Add on E-Commerce to sell products
• K7V Certification Program
• PulseCore tools & technology
• Totally MoRV Assessment Distributor
• 4 Crew Pattern Distributor

See attached document describing the updates.

Target Market(s)

Small-Large Business and Corporations
Public Sector Organizations

Industry/Entity Type

Leadership

Number of Pages Required

5+ page

Font styles to use
Other font styles liked:
• www.brightpath7gains.com

Requirements
Must have
• Wordpress expertise
• E-Commerce plugin expertise
• Website Maintenance capability
Nice to have
• Easy access to transfer documents and get feedback/suggestions on the best wording for presenting the information onto my site for each of the pages
Should not have
• Focus on changing the current design of my site

```html
<!DOCTYPE html>
<html lang="en">
<head>
<meta charset="utf-8">
<title>Brightpath7Gains — Developing Leadership Talent &amp; Succession</title>
<link href="https://fonts.googleapis.com/css2?family=Source+Sans+3:wght@300;400;600;700&display=swap" rel="stylesheet">
<style>
:root{
  --orange:#eaa52f;
  --orange-deep:#dc9216;
  --orange-soft:rgba(238,172,60,.86);
  --ink:#3a3a3a;
  --ink-soft:#4b4b4b;
  --white:#ffffff;
  --panel:#f4f4f4;
  --footer:#ebebeb;
  --teal:#3b9aa6;
  --blue:#4b77c0;
  --dark-btn:#3d3d3d;
}
*{margin:0;padding:0;box-sizing:border-box}
html,body{width:1200px;height:2381px;overflow:hidden}
body{position:relative;font-family:"Source Sans 3",sans-serif;color:var(--ink);background:var(--white)}
.abs{position:absolute}
.btn{position:absolute;display:flex;align-items:center;justify-content:center;font-size:16px;font-weight:600;letter-spacing:.3px;border-radius:3px;text-transform:uppercase}
.btn-orange{background:var(--orange);color:#5a3a08}
.btn-outline{border:2px solid #4a4a4a;color:#3f3f3f}
.btn-outline-light{border:2px solid #55606a;color:#3b4650}
.btn-dark{background:var(--dark-btn);color:var(--white);border-radius:3px}

/* Hero */
.hero{left:0;top:0;width:1200px;height:643px;background:linear-gradient(180deg,#7d97a3 0%,#8aa4af 40%,#6f8c99 75%,#4c6b7b 100%)}
.brand{left:0;top:35px;width:1200px;display:flex;justify-content:center;align-items:center;gap:8px}
.brand-mark{width:28px;height:28px;background:var(--orange)}
.brand-name{font-size:22px;font-weight:400;color:#3a3a3a}
.nav{left:56px;top:111px;width:1087px;height:54px;background:var(--orange);border:1px solid #c98a1a;display:flex;align-items:center;justify-content:space-around;padding:0 30px}
.nav a{font-size:17px;font-weight:600;color:#4a3208;text-decoration:none;text-transform:uppercase}
.nav a.active{color:var(--white)}
.hero-title{left:0;top:304px;width:1200px;text-align:center;font-size:42px;font-weight:600;color:var(--white);text-shadow:0 2px 6px rgba(0,0,0,.35)}
.dots{left:1132px;top:296px;display:flex;flex-direction:column;gap:6px}
.dots span{width:12px;height:12px;border-radius:50%;background:#2f3a42}
.dots span.on{background:#8a9aa3}
.hero-band{left:0;top:643px;width:1200px;height:16px;background:var(--orange)}
.scroll-tab{left:540px;top:582px;width:120px;height:77px;background:var(--orange-deep);display:flex;align-items:center;justify-content:center}

/* Team & welcome */
.team{left:0;top:659px;width:600px;height:344px;background:linear-gradient(160deg,#e9b35a,#e2a442 60%,#d99a38)}
.team-title{left:0;top:768px;width:600px;text-align:center;font-size:44px;font-weight:400;color:#4a3a20}
.welcome{left:600px;top:659px;width:600px;height:344px;background:var(--panel)}
.welcome h2{position:absolute;left:62px;top:60px;font-size:44px;font-weight:400;color:var(--ink)}
.welcome p{position:absolute;left:62px;top:130px;width:470px;font-size:17px;line-height:30px;color:var(--ink-soft)}

/* Services */
.services-title{left:0;top:1026px;width:1200px;text-align:center;font-size:44px;font-weight:400;color:var(--ink)}
.service{top:1140px;width:260px}
.service .icon{width:120px;height:120px;margin:0 auto;border-radius:50%;background:var(--orange);display:flex;align-items:center;justify-content:center;color:var(--white);font-size:72px;font-weight:700}
.service h3{margin-top:26px;text-align:center;font-size:27px;font-weight:400;color:var(--ink)}
.service p{margin-top:8px;font-size:17px;line-height:30px;color:var(--ink-soft)}

/* Feature bands */
.feature{display:flex;flex-direction:column;align-items:center;justify-content:center;color:var(--white);text-align:center}
.feature h2{font-size:44px;font-weight:400;line-height:48px;text-transform:uppercase}
.feature h2.dark{color:#3a3220}
.feature .btn{position:static;margin-top:18px;height:36px}
.feature-teal{left:0;top:1480px;width:600px;height:344px;background:linear-gradient(135deg,#4aa6ad,#2f8d99)}
.feature-blue{left:600px;top:1480px;width:600px;height:344px;background:linear-gradient(135deg,#5582c6,#3e69b4)}
.feature-orange{left:0;top:1824px;width:1200px;height:344px;background:linear-gradient(135deg,#f0b24c,#e9a53c 50%,#f1b552)}

/* Footer */
.footer{left:0;top:2168px;width:1200px;height:213px;background:var(--footer)}
.footer-brand{left:56px;top:2235px;display:flex;align-items:center;gap:10px}
.footer-brand .brand-mark{width:44px;height:44px;background:#8a8a8a}
.footer-brand .brand-name{font-size:34px;color:#4a4a4a}
.tagline{left:110px;top:2282px;font-size:11px;color:#555}
.copyright{left:56px;top:2332px;font-size:11px;color:#444}
.footer h4{position:absolute;top:2201px;font-size:17px;font-weight:600;color:#222}
.footer-small{position:absolute;font-size:11px;line-height:16px;color:#333}
.input{left:954px;top:2245px;width:189px;height:36px;border:2px solid #444;border-radius:4px;background:var(--white);font-size:14px;color:#aaa;padding:7px 12px}
</style>
</head>
<body>

<header class="abs hero" role="img" aria-label="Photograph of a suspension bridge disappearing into fog"></header>
<div class="abs brand"><span class="brand-mark"></span><span class="brand-name">Brightpath7Gains</span></div>
<nav class="abs nav">
  <a class="active" href="#">Home</a><a href="#">Approach</a><a href="#">Tools</a><a href="#">Assessments</a><a href="#">Clients</a><a href="#">Consultants</a><a href="#">Speaking</a><a href="#">Blog</a><a href="#">E-Learning Courses</a><a href="#">Contact B7G</a>
</nav>
<h1 class="abs hero-title">BUY OUR ONLINE COURSES</h1>
<a class="btn btn-orange" style="left:459px;top:383px;width:117px;height:35px">Buy Now</a>
<a class="btn btn-outline-light" style="left:600px;top:383px;width:141px;height:35px">Contact Us</a>
<div class="abs dots"><span></span><span class="on"></span><span class="on"></span><span></span></div>
<div class="abs hero-band"></div>
<div class="abs scroll-tab">
  <svg width="30" height="20" viewBox="0 0 30 20"><path d="M4 4 L15 15 L26 4" fill="none" stroke="#2a2a2a" stroke-width="5"/></svg>
</div>

<section class="abs team" role="img" aria-label="Photograph of a smiling business team with arms crossed, tinted orange"></section>
<h2 class="abs team-title">PROFESSIONAL TEAM</h2>
<a class="btn btn-dark" style="left:122px;top:848px;width:167px;height:35px">Meet the Team</a>
<a class="btn btn-outline" style="left:314px;top:848px;width:140px;height:35px">Contact Us</a>

<section class="abs welcome">
  <h2>WELCOME</h2>
  <p>Thank you for your choice. We can help you solve any problem because we provide only rational solutions. We can satisfy clients with different requirements. So don't waste your precious time on hesitations.</p>
</section>
<a class="btn btn-orange" style="left:662px;top:924px;width:143px;height:35px">Learn More</a>

<h2 class="abs services-title">SERVICES</h2>
<div class="abs service" style="left:54px"><div class="icon">A</div><h3>TITLE 04</h3><p>Thank you for your choice. We can help you solve any problem because we provide only rational solutions. We can satisfy clients.</p></div>
<div class="abs service" style="left:332px"><div class="icon">A</div><h3>TITLE 02</h3><p>Thank you for your choice. We can help you solve any problem because we provide only rational solutions. We can satisfy clients.</p></div>
<div class="abs service" style="left:610px"><div class="icon">A</div><h3>TITLE 03</h3><p>Thank you for your choice. We can help you solve any problem because we provide only rational solutions. We can satisfy clients.</p></div>
<div class="abs service" style="left:888px"><div class="icon">A</div><h3>TITLE 04</h3><p>Thank you for your choice. We can help you solve any problem because we provide only rational solutions. We can satisfy clients.</p></div>

<section class="abs feature feature-teal" role="img" aria-label="Collage of web search logos in perspective, tinted teal">
  <h2>K7V License &amp;<br>Certification</h2><a class="btn btn-dark" style="width:168px">Learn More</a>
</section>
<section class="abs feature feature-blue" role="img" aria-label="Collage of web search logos in perspective, tinted blue">
  <h2>PulseCore Trainer</h2><a class="btn btn-dark" style="width:168px">Learn More</a>
</section>
<section class="abs feature feature-orange" role="img" aria-label="Collage of web search logos in perspective, tinted orange">
  <h2 class="dark">4 Crew Patterns Training</h2><a class="btn btn-dark" style="width:168px">Learn More</a>
</section>

<footer class="abs footer"></footer>
<div class="abs footer-brand"><span class="brand-mark"></span><span class="brand-name">Brightpath7Gains</span></div>
<div class="abs tagline">Developing Leadership Talent &amp; Succession</div>
<div class="abs copyright">© Copyright 2016. <b>Brightpath7Gains, LLC</b> | All Rights Reserved.</div>

<h4 style="left:532px">Contact</h4>
<div class="footer-small" style="left:532px;top:2248px;font-weight:600">St: Lorem ipsum<br>Lindenvale, Norland.</div>
<div class="footer-small" style="left:532px;top:2292px">(555) 014-2273</div>
<div class="footer-small" style="left:532px;top:2320px">nora@brightpath7gains.com</div>

<h4 style="left:729px">Testimonials</h4>
<div class="footer-small" style="left:729px;top:2248px;font-weight:600">Name Surname, <i style="font-weight:400">City, State</i></div>
<div class="footer-small" style="left:729px;top:2262px;font-size:9px">25th Nov 2015</div>
<div class="footer-small" style="left:729px;top:2278px;width:160px;color:#666">"Lorem ipsum dolor sit amet, consectetur adipisicing elit, es sed do eiusmod tempor etro incidieprollo"</div>

<h4 style="left:954px">Newsletter</h4>
<div class="abs input">Email</div>
<a class="btn btn-dark" style="left:954px;top:2298px;width:132px;height:37px">Subscribe</a>

</body>
</html>
```